TernQuay Business Cards

Create business cards for our exciting new software company. We provide cloud billing systems and provisioning software for campany that need monthly SaaS and Cloud Billing

Target Market(s)

Enterprise businesses, b2b, telecom carriers, software manufactures

Industry/Entity Type

Software

```html
<!DOCTYPE html>
<html lang="en">
<head>
<meta charset="utf-8">
<title>TernQuay Business Cards</title>
<link rel="stylesheet" href="https://fonts.googleapis.com/css2?family=Questrial&family=Arimo:wght@400&display=swap">
<style>
  :root {
    --backdrop: #4a4a4c;
    --card-navy: #213654;
    --card-white: #f1f2f3;
    --sky: #7cc0dc;
    --steel: #3b6a8e;
    --ink: #1f3350;
    --muted: #8a96a3;
    --tagline-light: #c9d6e2;
    --tagline-dark: #4d5966;
  }
  * { margin: 0; padding: 0; box-sizing: border-box; }
  html, body {
    width: 1200px;
    height: 900px;
    overflow: hidden;
    background: var(--backdrop);
  }
  .canvas {
    position: relative;
    width: 1200px;
    height: 900px;
  }
  .card {
    position: absolute;
    top: 300px;
    width: 525px;
    height: 300px;
    border-radius: 22px;
    overflow: hidden;
  }
  .card--front { left: 58px; background: var(--card-navy); }
  .card--back  { left: 617px; background: var(--card-white); }

  .wordmark {
    position: absolute;
    font-family: "Questrial", sans-serif;
    font-weight: 400;
    line-height: 1;
    letter-spacing: 0.5px;
    white-space: nowrap;
  }
  .tagline {
    position: absolute;
    font-family: "Questrial", sans-serif;
    font-size: 6.6px;
    line-height: 9px;
    letter-spacing: 1.1px;
    text-transform: uppercase;
    text-align: right;
    white-space: nowrap;
  }

  /* Front */
  .card--front .wordmark {
    right: 253px;
    top: 198px;
    font-size: 36px;
    color: var(--sky);
  }
  .card--front .tagline {
    right: 253px;
    top: 238px;
    color: var(--tagline-light);
  }
  .card--front .site {
    position: absolute;
    left: 50px;
    top: 266px;
    font-family: "Questrial", sans-serif;
    font-size: 11px;
    letter-spacing: 3.6px;
    color: var(--tagline-light);
  }

  /* Back */
  .card--back .wordmark {
    right: 49px;
    top: 134px;
    font-size: 30px;
    color: var(--steel);
  }
  .card--back .tagline {
    right: 49px;
    top: 166px;
    color: var(--tagline-dark);
  }
  .contact {
    position: absolute;
    right: 49px;
    top: 194px;
    text-align: right;
    font-family: "Arimo", sans-serif;
    color: var(--ink);
  }
  .contact__name {
    font-size: 13.5px;
    letter-spacing: 0.8px;
    line-height: 15px;
  }
  .contact__role {
    font-size: 9px;
    line-height: 12px;
    margin-bottom: 3px;
  }
  .contact__line {
    font-size: 11px;
    line-height: 13.5px;
  }
  .contact__label { color: var(--muted); }
  .contact__site {
    font-size: 11px;
    line-height: 13.5px;
    margin-top: 3px;
  }
</style>
</head>
<body>
  <main class="canvas">
    <section class="card card--front" aria-label="Business card front">
      <div class="wordmark">TernQuay</div>
      <div class="tagline">Cloud billing and<br>operational support systems</div>
      <div class="site">www.TernQuay.com</div>
    </section>

    <section class="card card--back" aria-label="Business card back">
      <div class="wordmark">TernQuay</div>
      <div class="tagline">Cloud billing and<br>operational support systems</div>
      <div class="contact">
        <div class="contact__name">NORA VALE</div>
        <div class="contact__role">CEO</div>
        <div class="contact__line">TernQuay</div>
        <div class="contact__line">2417 Harbor Lane, Easton, MD 21601</div>
        <div class="contact__line"><span class="contact__label">P:</span> 410.555.2700 x 2704 <span class="contact__label">F:</span> 410.555.2701</div>
        <div class="contact__site">www.TERNQUAY.com</div>
      </div>
    </section>
  </main>
</body>
</html>
```